Need a tea box packaging design

* Organic Herbal tea
* Imported from india to france for european community
* our main rivals are " ZENDRA" tea and " BRAVO" tea.
* the product will be sold online and shops.
* 15 variety of teas will be imported.
* The details in the attached file.
The Packaging contents:
Main page :
Brand Name : KORIL ( logo attached)
Name of the product: KELORA THE NOIR ( which means Kelora black tea)
Type of the product : Infusion
No of tea bags : 20
Weight of each bag : 1,5 gm
Total weight : 30 gm
Organic label name : Europe ( organic logo attached)
vegan label : vegan ( vegan label attached)
The other side contents will be given later.
A model that i have designed with another designer is attached. It is nice. But i am expecting more than that. ( attached)
Some designs that i like are attached here.
As mentionned earlier there will 15 variety of teas, so the design should easily modifiable by just changing colours.
Updates
Project Deadline Extended Reason: I think the deadline is very short due to the weekend. So, I feel it is better to extend the deadline by 5 days. Added Saturday, January 21, 2017
Target Market(s)
Europe. Mainly france.
Industry/Entity Type
Community
Requirements
Must have
- * Design should be modern and colourfull.
- * I like pattern works, Vectorials
- * Yoga silouhaites in the design is appreciable.
- * The design should express wellness, joy and love
Nice to have
- "Zendra" tea in my inspirational design.
- * The ingredients can be showed in vectorial designs in the back ground.
- * The end user must see the box while taking the tea and appreciate
- * The end user must search and find some hidden things.
- * The box must be communicative.
- * Trendy frames.
Should not have
- No need to have tea cups

```html
<!DOCTYPE html>
<html lang="en">
<head>
<meta charset="utf-8">
<title>Kelora The Noir – Tea Box Panels</title>
<link href="https://fonts.googleapis.com/css2?family=Pathway+Gothic+One&family=Great+Vibes&family=Crimson+Text:wght@400;700&display=swap" rel="stylesheet">
<style>
  :root{
    --stage:#e4e4e7;
    --purple:#421a5c;
    --purple-deep:#34124a;
    --purple-soft:#5b2a7c;
    --pink:#f0236f;
    --pink-soft:#f45b8c;
    --peach:#f7a98a;
    --lilac:#9a5cc9;
    --white:#ffffff;
    --organic:#8cc63f;
  }
  *{box-sizing:border-box;margin:0;padding:0}
  html,body{width:1200px;height:853px;overflow:hidden;background:var(--stage)}
  .stage{position:relative;width:1200px;height:853px}
  .panel{position:absolute;background:var(--purple);overflow:hidden;color:var(--white);text-align:center}
  .panel--front{left:150px;top:124px;width:430px;height:610px}
  .panel--back{left:700px;top:100px;width:310px;height:660px}

  /* front */
  .mandala{position:absolute;left:-45px;top:-184px;width:520px;height:520px;border-radius:50%;
    background:radial-gradient(circle,var(--purple-deep) 0 48px,var(--lilac) 49px,var(--pink-soft) 32%,var(--peach) 48%,var(--pink) 60%,var(--lilac) 72%,var(--pink-soft) 86%,var(--peach) 100%)}
  .brand{position:absolute;left:167px;top:28px;width:96px;height:96px;border-radius:50%;background:var(--purple-deep);
    display:flex;align-items:center;justify-content:center;font-family:"Pathway Gothic One",sans-serif;font-size:24px;letter-spacing:2px;color:var(--white)}
  .product-name{position:absolute;left:0;width:100%;font-family:"Great Vibes",cursive;font-weight:400;color:var(--white);line-height:1;text-shadow:0 3px 8px rgba(52,18,74,.6)}
  .panel--front .product-name{top:190px;font-size:132px}
  .yoga{position:absolute;top:340px;height:84px;background:var(--pink);opacity:.85;border-radius:40px 40px 0 0}
  .yoga--left{left:30px;width:80px}
  .yoga--right{left:310px;width:110px}
  .variant{position:absolute;left:0;width:100%;font-family:"Pathway Gothic One",sans-serif;color:var(--pink-soft);letter-spacing:1px}
  .panel--front .variant{top:366px;font-size:32px}
  .subtitle{position:absolute;left:0;width:100%;font-family:"Pathway Gothic One",sans-serif;letter-spacing:2px}
  .panel--front .subtitle{top:404px;font-size:17px}
  .flavour-band{position:absolute;left:0;top:426px;width:100%;height:38px;background:var(--pink);
    font-family:"Pathway Gothic One",sans-serif;font-size:27px;line-height:38px;letter-spacing:.5px}
  .type{position:absolute;left:0;width:100%;font-family:"Great Vibes",cursive;color:var(--white)}
  .panel--front .type{top:474px;font-size:40px}
  .net-weight{position:absolute;left:22px;top:552px;text-align:left;font-family:"Pathway Gothic One",sans-serif;font-size:20px;line-height:23px}
  .badge-vegan{position:absolute;left:282px;top:552px;width:50px;height:46px;border-radius:50%;background:var(--white);opacity:.85}
  .badge-organic{position:absolute;left:348px;top:550px;width:66px;height:48px;background:var(--organic)}

  /* back */
  .edge-pattern{position:absolute;right:-40px;top:16px;width:80px;height:270px;border-radius:40px;
    background:linear-gradient(180deg,var(--pink-soft),var(--peach) 40%,var(--pink) 70%,var(--lilac))}
  .panel--back .product-name{top:50px;font-size:96px}
  .panel--back .variant{top:180px;font-size:24px}
  .panel--back .subtitle{top:210px;font-size:13px}
  .panel--back .type{top:230px;font-size:30px}
  .steps{position:absolute;left:42px;top:280px;width:226px;height:90px;display:flex;gap:10px}
  .step{flex:1;border-radius:10px;background:var(--purple-soft)}
  .directions{position:absolute;left:36px;top:402px;width:238px;font-family:"Crimson Text",serif;font-size:11.5px;line-height:15.5px}
  .divider{position:absolute;left:125px;top:462px;width:60px;height:1px;background:var(--pink-soft)}
  .pitcher{position:absolute;left:36px;top:510px;width:70px;height:86px;border-radius:10px;background:var(--purple-soft)}
  .iced{position:absolute;left:112px;top:486px;width:172px;font-family:"Crimson Text",serif;font-size:11.5px;line-height:15.2px}
  .iced strong,.directions strong{font-weight:700}
</style>
</head>
<body>
<main class="stage">
  <section class="panel panel--front">
    <div class="mandala" role="img" aria-label="Radiating mandala of pink, peach and violet leaf petals"></div>
    <div class="brand">KORIL</div>
    <h1 class="product-name">kelora</h1>
    <div class="yoga yoga--left" role="img" aria-label="Pink yoga pose silhouettes"></div>
    <div class="yoga yoga--right" role="img" aria-label="Pink yoga pose silhouettes"></div>
    <p class="variant">THE NOIR</p>
    <p class="subtitle">- KELORA BLACK TEA -</p>
    <p class="flavour-band">MORINGA APPLE CINAMON INFUSION</p>
    <p class="type">Infusion</p>
    <p class="net-weight">NET WT.:<br>30G (20x1.5G) e</p>
    <div class="badge-vegan" role="img" aria-label="Vegan label"></div>
    <div class="badge-organic" role="img" aria-label="EU organic label"></div>
  </section>

  <section class="panel panel--back">
    <div class="edge-pattern" role="img" aria-label="Leaf petal pattern along the edge"></div>
    <h2 class="product-name">kelora</h2>
    <p class="variant">THE NOIR</p>
    <p class="subtitle">- KELORA BLACK TEA -</p>
    <p class="type">Infusion</p>
    <div class="steps">
      <div class="step" role="img" aria-label="Step 1 drawing: pouring boiling water"></div>
      <div class="step" role="img" aria-label="Step 2 drawing: adding a tea bag"></div>
      <div class="step" role="img" aria-label="Step 3 drawing: letting it infuse"></div>
    </div>
    <p class="directions"><strong>Directions:</strong> Pour boiling water over tea bag in your cup or teapot (1 bag per cup) and infuse for 5-7 minutes. If you prefer, sweeten with sugar or honey.</p>
    <div class="divider"></div>
    <div class="pitcher" role="img" aria-label="Line drawing of an iced tea pitcher and glass"></div>
    <p class="iced"><strong>For 1 liter of iced Tea:</strong><br>Pour 1/2 liter of boiling water over 8 tea bags, cover and infuse for 20 minutes. Remove tea bags, add 1/2 liter of cold water and refrigerate. Pour over ice to server.</p>
  </section>
</main>
</body>
</html>
```